Verpackungsdesign für Outdoor-Produkt
Lurvo suchte ein neues Design in der Kategorie Verpackungen und hat ein Projekt auf gestaltwerk-portal.de gestartet.
Zielgruppe
Wir verkaufen einzigartige Outdoor Produkte. Der Feuerstahl richtet sich an alle, die gerne in der Natur übernachten und beim Feuermachen noch selbst Hand anlegen wollen. Die Zielgruppe interessiert sich für Bushcraft & Survival, ist größtenteils Männlich und zwischen 30-40 Jahre alt.
Aufgabenstellung
Auf die obere Seite der Verpackung sollen das Logo und der Produktname platziert werden. Das Produkt gibt es in zwei Varianten, deshalb auch zwei verschiedene Namen.
Auf der vorderen Seite sollen die Features hervorgehoben werden. Dafür zum Beispiel ein passendes Icon finden und die Eigenschaft dazu (Beispiel: 'Flammen'-Icon, Bis zu 20.000 Zündungen garantiert).
An den Seiten links und rechts reicht das Logo.
Auf die hintere Seite kommt das Impressum.
Die Verpackung besteht aus braunem Karton.

```html
<!DOCTYPE html>
<html lang="de">
<head>
<meta charset="utf-8">
<title>Lurvo „Kiefer“ Feuerstahl – Verpackung</title>
<link href="https://fonts.googleapis.com/css2?family=Oswald:wght@500&family=Roboto+Slab:wght@400;700&display=swap" rel="stylesheet">
<style>
  :root {
    --page: #f4f4f2;
    --kraft: #c9a878;
    --kraft-edge: #b8966a;
    --ink: #2b2a28;
  }
  * { margin: 0; padding: 0; box-sizing: border-box; }
  html, body { width: 1200px; height: 675px; overflow: hidden; background: var(--page); }
  body {
    display: flex; flex-direction: column; align-items: center; justify-content: center; gap: 36px;
    font-family: "Roboto Slab", serif; color: var(--ink);
  }
  .panel {
    width: 1060px; background: var(--kraft); border: 1px solid var(--kraft-edge);
  }
  .panel--front {
    height: 250px; display: grid; grid-template-columns: repeat(4, 1fr);
    align-items: start; padding: 50px 50px 0;
  }
  .feature { text-align: center; display: flex; flex-direction: column; align-items: center; }
  .feature__icon { height: 48px; display: flex; align-items: flex-end; margin-bottom: 10px; }
  .feature__icon svg { stroke: var(--ink); fill: none; stroke-width: 2; stroke-linejoin: round; stroke-linecap: round; }
  .feature__title { font-weight: 700; font-size: 17px; line-height: 1.15; letter-spacing: 0.02em; margin-bottom: 8px; }
  .feature__text { font-size: 14px; line-height: 1.3; }
  .panel--top {
    height: 200px; display: flex; flex-direction: column; align-items: center; justify-content: center; gap: 26px;
  }
  .brand { display: flex; align-items: center; gap: 10px; font-family: "Roboto Slab", serif; font-size: 20px; font-weight: 400; letter-spacing: 0.2em; }
  .brand__dot { width: 12px; height: 12px; border: 2px solid var(--ink); border-radius: 50%; }
  .product-name { font-family: "Oswald", sans-serif; font-weight: 500; font-size: 44px; letter-spacing: 0.06em; }
</style>
</head>
<body>
  <section class="panel panel--front">
    <div class="feature">
      <div class="feature__icon">
        <svg width="52" height="46" viewBox="0 0 52 46">
          <path d="M10 2 Q11 8 16 9 Q11 10 10 16 Q9 10 4 9 Q9 8 10 2Z"/>
          <path d="M20 20 Q21 28 28 29 Q21 30 20 38 Q19 30 12 29 Q19 28 20 20Z"/>
          <path d="M40 12 Q41 17 45 18 Q41 19 40 24 Q39 19 35 18 Q39 17 40 12Z"/>
        </svg>
      </div>
      <div class="feature__title">3000 °C HEIßE<br>FUNKEN</div>
      <div class="feature__text">Mehr als 20.000<br>Zündungen garantiert</div>
    </div>
    <div class="feature">
      <div class="feature__icon">
        <svg width="64" height="30" viewBox="0 0 64 30"><rect x="3" y="9" width="58" height="10" transform="rotate(12 32 14)"/></svg>
      </div>
      <div class="feature__title">XXL<br>ZÜNDSTAB</div>
      <div class="feature__text">12,7 cm lang,<br>1,27 cm Durchmesser</div>
    </div>
    <div class="feature">
      <div class="feature__icon">
        <svg width="60" height="26" viewBox="0 0 60 26">
          <path d="M4 20 Q20 4 40 6 L56 6 L56 16 L40 16 Q24 16 4 20Z"/>
          <circle cx="49" cy="11" r="2"/>
        </svg>
      </div>
      <div class="feature__title">SURVIVAL STRIKER</div>
      <div class="feature__text">Hochwertiger 8Cr13MoV Stahl,<br>läßt sich im Notfall sogar zu<br>Mini Messer schärfen</div>
    </div>
    <div class="feature">
      <div class="feature__icon">
        <svg width="130" height="40" viewBox="0 0 130 40">
          <path d="M4 12 H30 Q36 12 36 7 Q36 3 32 3"/>
          <path d="M4 20 H40"/>
          <path d="M10 28 H28 Q33 28 33 33"/>
          <path d="M60 14 Q54 24 54 28 A6 6 0 0 0 66 28 Q66 24 60 14Z"/>
          <path d="M78 8 Q73 16 73 20 A5 5 0 0 0 83 20 Q83 16 78 8Z"/>
          <path d="M112 6 V34 M100 13 L124 27 M100 27 L124 13"/>
        </svg>
      </div>
      <div class="feature__title">WIND-/WASSER-/<br>KÄLTE-RESIST</div>
      <div class="feature__text">Schutz bei<br>allen Witterungen</div>
    </div>
  </section>

  <section class="panel panel--top">
    <div class="brand"><span class="brand__dot"></span>LURVO</div>
    <h1 class="product-name">LURVO „KIEFER“ FEUERSTAHL</h1>
  </section>
</body>
</html>
```